High end business card design for custom homebuilding company

Looking for a high end business card design that is unique and elegant. Can use embossing, foil printing, laser die cutting, or any high end printing technique or high end paper. Will upload current design so you can see the logo and what we are using currently, but we want something more unique and elegant. I included our logo to help with design.

Target Market(s)

High end custom home buyers of $1.5 million plus homes. Also real estate developers of high end communities.

Industry/Entity Type

Business

Contact Information for Business Card

Double sided. We want something very elegant and expensive looking. We are looking to incorporate a combination of perhaps linen paper or a high end paper, with foil stamping or embossing/debossing to make the card look unique, but still elegant. We tend to use blacks and golds, but are open to any ideas. Looking for creative and unique design.

Colors

Designer to choose colors to be used in the design.

Requirements
Must have
• High end, elegant look. Can use foil, embossing, or high end papers like linen. We want to make the card unique and interesting, but elegant and expensive looking.
Nice to have
• I am including just some cards I saw that looked interesting for one reason or another. I like a clean elegant design and like both the clean white style, and the blacks. So not sure if we want a black design or white. Would like to see both.

```html
<!DOCTYPE html>
<html lang="en">
<head>
<meta charset="utf-8">
<title>Ridgeline Custom Homes – Business Cards</title>
<link rel="stylesheet" href="https://fonts.googleapis.com/css2?family=Montserrat:wght@400;500;600&display=swap">
<style>
  :root {
    --backdrop: #5a5a5a;
    --paper: #fbfbfa;
    --ink: #1f1e1c;
    --ink-soft: #262524;
    --gold: #b4952f;
    --gold-light: #d2b24a;
    --text-light: #f2f2f2;
    --text-muted: #d9d9d9;
  }
  * { box-sizing: border-box; margin: 0; padding: 0; }
  html, body {
    width: 1200px; height: 1134px; overflow: hidden;
    background: var(--backdrop);
    font-family: "Montserrat", sans-serif;
  }
  .card {
    position: absolute;
    left: 261px;
    width: 675px;
    box-shadow: 0 6px 14px rgba(0,0,0,0.45);
    overflow: hidden;
  }
  .card-front { top: 161px; height: 379px; background: var(--paper); }
  .card-back  { top: 589px; height: 384px; background: var(--ink); }

  .front-shape { position: absolute; inset: 0; }

  .brand {
    position: absolute;
    display: flex; align-items: center; gap: 10px;
    font-weight: 600;
    letter-spacing: 1px;
    text-transform: uppercase;
    white-space: nowrap;
  }
  .brand-dot { width: 14px; height: 14px; border-radius: 50%; background: var(--gold); }
  .card-front .brand { left: 38px; top: 56px; font-size: 22px; color: var(--ink); }
  .card-back .brand { left: 0; right: 0; top: 168px; justify-content: center; font-size: 30px; color: var(--gold-light); }

  .contact {
    position: absolute; right: 37px; top: 0;
    text-align: right; color: var(--text-light);
  }
  .contact-name { position: absolute; right: 0; top: 160px; font-size: 27px; font-weight: 500; white-space: nowrap; }
  .contact-address { position: absolute; right: 0; top: 218px; font-size: 14.5px; line-height: 20px; white-space: nowrap; color: var(--text-muted); }
  .contact-lines { position: absolute; right: 0; top: 282px; list-style: none; font-size: 14.5px; color: var(--text-muted); }
  .contact-lines li { display: flex; justify-content: flex-end; align-items: center; gap: 10px; height: 23px; white-space: nowrap; }
  .contact-lines svg { width: 15px; height: 15px; fill: var(--gold); flex: none; }

  .back-pattern {
    position: absolute; inset: 0;
    background: linear-gradient(90deg, var(--ink) 0%, #2a2928 45%, #333230 75%, var(--ink-soft) 100%);
  }
  .back-web {
    position: absolute; left: 0; right: 0; top: 320px;
    text-align: center; font-size: 15px; color: var(--text-muted); letter-spacing: 0.3px;
  }
</style>
</head>
<body>

<section class="card card-front">
  <svg class="front-shape" viewBox="0 0 675 379" width="675" height="379" aria-hidden="true">
    <path d="M592,86 C380,120 165,230 85,379 L123,379 C205,225 420,110 675,74 L675,72 C640,76 615,81 592,86 Z" fill="var(--gold)"/>
    <path d="M675,74 C420,110 205,225 123,379 L675,379 Z" fill="var(--ink)"/>
  </svg>

  <div class="brand"><span class="brand-dot"></span>Ridgeline Custom Homes</div>

  <div class="contact">
    <p class="contact-name">Dummy Name</p>
    <p class="contact-address">Level 5, 27 Harrow Lane<br>Melbourne, VIC 3000</p>
    <ul class="contact-lines">
      <li>123 456 7890
        <svg viewBox="0 0 16 16"><path d="M3.5 1.5l2.5 0 1 3.5-1.8 1.2c.9 1.9 2.4 3.4 4.3 4.3L10.7 8.7l3.5 1v2.6c0 .9-.8 1.6-1.7 1.5C6.8 13.3 2.4 8.9 2 3.2 1.9 2.3 2.6 1.5 3.5 1.5z"/></svg>
      </li>
      <li>123 456 7890
        <svg viewBox="0 0 16 16"><path d="M5 1h6a1.2 1.2 0 0 1 1.2 1.2v11.6A1.2 1.2 0 0 1 11 15H5a1.2 1.2 0 0 1-1.2-1.2V2.2A1.2 1.2 0 0 1 5 1zm.3 1.8v9h5.4v-9zM8 12.6a.8.8 0 1 0 0 1.6.8.8 0 0 0 0-1.6z"/></svg>
      </li>
      <li>info@ridgelinecustomhomes.com.au
        <svg viewBox="0 0 16 16"><path d="M1 3.5h14v9H1zm1.4 1l5.6 4.3 5.6-4.3z"/></svg>
      </li>
      <li>www.ridgelinecustomhomes.com.au
        <svg viewBox="0 0 16 16"><path d="M8 1a7 7 0 1 0 0 14A7 7 0 0 0 8 1zm0 1.5c.8.8 1.4 2.2 1.6 4H6.4C6.6 4.7 7.2 3.3 8 2.5zM5 6.5H2.6A5.5 5.5 0 0 1 5.8 3 8 8 0 0 0 5 6.5zm0 3a8 8 0 0 0 .8 3.5 5.5 5.5 0 0 1-3.2-3.5zm1.4 0h3.2c-.2 1.8-.8 3.2-1.6 4-.8-.8-1.4-2.2-1.6-4zm4.6 0h2.4a5.5 5.5 0 0 1-3.2 3.5 8 8 0 0 0 .8-3.5zm0-3a8 8 0 0 0-.8-3.5 5.5 5.5 0 0 1 3.2 3.5z"/></svg>
      </li>
    </ul>
  </div>
</section>

<section class="card card-back">
  <div class="back-pattern" role="img" aria-label="Faint repeating brand-mark pattern across the card background"></div>
  <div class="brand"><span class="brand-dot"></span>Ridgeline Custom Homes</div>
  <p class="back-web">www.ridgelinecustomhomes.com.au</p>
</section>

</body>
</html>
```